Business Card Design Project

I need a business card designed that is clean, simple and elegant.
I am a fashion and advertising photographer based in Cape Town and Durban South Africa.
check out my website: www.brennowalsh.co.za for ideas
Updates
Hi all,
Thanks for your submissions so far!
Please note:
I want no more than than black, white and/or grey to be used.
I don't want any photos used.
I would like the card to be double sided.
I would like to continue the design similar to the past ones Ive used.
I hope this helps, please send me further questions should you have any.
many thanks!
Brenno
Hi,
Please have a look at the jpg I loaded(called inspiration) which is the direction or inspiration I am aiming at.
Also PLEASE remember NO PHOTOS to be included on the card
many thanks!!
Target Market(s)
You can look at my site to get a better understanding of the audience:
www.brennowalsh.co.za
Industry/Entity Type
Advertising
Requirements
Must have
- Clean design which can also be used for a watermark on photographs
perhaps black background with white text/grey
company called: Brenno Walsh Photography
Nice to have
- below I have added logos that I have used in the past.
Should not have
- pictures of cameras
tacky elements

```html
<!DOCTYPE html>
<html lang="en">
<head>
<meta charset="utf-8">
<title>Brenno Walsh Photography – Business Card</title>
<link rel="stylesheet" href="https://fonts.googleapis.com/css2?family=Lato:wght@400;700;900&display=swap">
<style>
  :root {
    --backdrop: #141414;
    --card: #1e1d1e;
    --ink-light: #ececec;
    --ink-soft: #d6d6d6;
  }
  html, body {
    margin: 0;
    padding: 0;
    width: 1200px;
    height: 984px;
    overflow: hidden;
    background: var(--backdrop);
  }
  .sheet {
    position: relative;
    width: 1200px;
    height: 984px;
  }
  .card {
    position: absolute;
    left: 220px;
    width: 760px;
    height: 434px;
    background: var(--card);
    border-radius: 22px;
    box-sizing: border-box;
    font-family: "Lato", sans-serif;
  }
  .card--back { top: 38px; }
  .card--front { top: 512px; }

  .wordmark {
    position: absolute;
    left: 110px;
    top: 50%;
    transform: translateY(-50%);
    margin: 0;
    font-weight: 900;
    font-size: 58px;
    line-height: 0.92;
    letter-spacing: 1px;
    text-transform: uppercase;
    color: var(--ink-light);
  }
  .wordmark span { display: block; }

  .holder-name {
    position: absolute;
    left: 0;
    right: 0;
    top: 150px;
    margin: 0;
    text-align: center;
    font-weight: 700;
    font-size: 50px;
    letter-spacing: 0.5px;
    color: var(--ink-light);
    padding-left: 90px;
  }
  .contact-row {
    position: absolute;
    left: 40px;
    right: 40px;
    bottom: 42px;
    display: flex;
    justify-content: space-between;
    margin: 0;
    padding: 0;
    list-style: none;
    font-weight: 400;
    font-size: 20px;
    color: var(--ink-soft);
  }
</style>
</head>
<body>
  <main class="sheet">
    <section class="card card--back" aria-label="Card back">
      <h1 class="wordmark">
        <span>Brenno</span>
        <span>Walsh</span>
        <span>Photography</span>
      </h1>
    </section>

    <section class="card card--front" aria-label="Card front">
      <h2 class="holder-name">Brenno Walsh</h2>
      <ul class="contact-row">
        <li class="contact-phone">+00 123 456 789</li>
        <li class="contact-email">office@brennowalsh.co.za</li>
        <li class="contact-web">www.brennowalsh.co.za</li>
      </ul>
    </section>
  </main>
</body>
</html>
```